Brightvale Relish Co, Bold Crunch Delight

We need a sticker that has Typograph and pickle man with a game controller in the sticker.
I would like “Brightvale Relish Co” on the sticker.
The slogan is “Bold Crunch Delight” so that need to be on the sticker as well.
We can make each letter a different color. I will sent picture as example.
I need my social media information on the sticker as well. (Instagram logo) @brightvalerelishco and (fb logo) brightvalerelishco.
The pickle man can be facing forward with a game controller as if he was playing.

Target Market(s)

Kids/Pickle Lovers

Industry/Entity Type

Food

Font styles to use
Decorative

Colors
0054AA
0677BA
7BADD7
CADEEF
E8F1F8
00AB8E
00BBA5
67D7C9
C6EFE9
E9F9F6
59FF00
82FF00
B8FF75
E3FFCB
F4FFEA
FFF300
FFF600
FEFA6F
FFFEC7
FFFEE8
F0912C
F2A743
F7CA91
FBE8D2
FDF5EE
EB3D1F
EC4F4E
F09395
F8D3D4
FCEDEE
E54698
E96AAD
F1A4CE
F9D9EA
FCEFF6
6B429C
8869AF
B7A5CE
E3DAEB
F3F0F8

Requirements
Must have
• A pickle holding a gaming control and my social media. Colorful
Nice to have
• Social Media and the pickle guy with gaming controller.

```html
<!DOCTYPE html>
<html lang="en">
<head>
<meta charset="utf-8">
<title>Brightvale Relish Co — Sticker Sheet</title>
<link rel="stylesheet" href="https://fonts.googleapis.com/css2?family=Fredoka:wght@700&family=Nunito:wght@800;900&display=swap">
<style>
  :root{
    --sheet:#bcbcbc;
    --sticker-edge:#ffffff;
    --band:#e8401f;
    --band-text:#ffffff;
    --slogan:#151515;
    --wordmark-bright:#fff600;
    --pickle-light:#9fce3c;
    --pickle-dark:#3f7f1f;

    --red-deep:#8c0c1c; --red-mid:#c8102e; --red-light:#e8506a;
    --green-deep:#0b4f26; --green-mid:#137a3a; --green-light:#1fa24e;
    --lime-deep:#2d8f2f; --lime-mid:#6cb63a; --lime-light:#c6dc52;
    --purple-deep:#5e2c86; --purple-mid:#8a3fa0; --purple-light:#b45cb4;
    --blue-deep:#0a4a86; --blue-mid:#0d64aa; --blue-light:#1f94d8;
  }
  *{box-sizing:border-box;margin:0;padding:0}
  html,body{width:1200px;height:1200px;overflow:hidden;background:var(--sheet)}
  .sheet{position:relative;width:1200px;height:1200px}
  .sticker{
    position:absolute;width:244px;height:204px;
    background:var(--sticker-edge);border-radius:22px;
  }
  .card{
    position:absolute;left:9px;top:9px;width:226px;height:186px;
    border-radius:13px;overflow:hidden;
  }
  .mascot{
    position:absolute;left:12px;top:14px;width:62px;height:138px;
    border-radius:30px 30px 22px 22px;
    background:linear-gradient(160deg,var(--pickle-light),var(--pickle-dark));
  }
  .wordmark{
    position:absolute;left:74px;top:18px;width:150px;
    font-family:"Fredoka",sans-serif;font-weight:700;
    font-size:25px;line-height:33px;letter-spacing:.2px;
    color:var(--wordmark-bright);text-transform:uppercase;
  }
  .slogan{
    position:absolute;left:74px;top:127px;width:150px;
    font-family:"Nunito",sans-serif;font-weight:900;font-size:10.5px;
    color:var(--slogan);text-transform:uppercase;letter-spacing:.1px;
    text-shadow:0 0 2px #fff,0 0 2px #fff;
  }
  .social-band{
    position:absolute;left:0;top:159px;width:100%;height:21px;
    background:var(--band);display:flex;justify-content:space-around;align-items:center;
    padding:0 6px;
  }
  .social{
    display:flex;align-items:center;gap:3px;
    font-family:"Nunito",sans-serif;font-weight:800;font-size:8px;color:var(--band-text);
  }
  .social .dot{width:8px;height:8px;border-radius:50%;border:1.5px solid var(--band-text)}
  .social .square{width:8px;height:8px;border-radius:2px;background:var(--band-text)}

  .col-1{left:152px}.col-2{left:477px}.col-3{left:804px}
  .row-1{top:72px}.row-2{top:285px}.row-3{top:498px}.row-4{top:711px}.row-5{top:923px}

  .red.burst{background:linear-gradient(115deg,var(--red-mid) 20%,#f3c9cf 60%,#fff 85%)}
  .red.deep{background:linear-gradient(115deg,var(--red-mid),var(--red-deep))}
  .red.glow{background:linear-gradient(115deg,var(--red-deep),var(--red-light))}
  .green.burst{background:linear-gradient(115deg,var(--green-deep) 20%,#cfe3d4 60%,#fff 85%)}
  .green.deep{background:linear-gradient(115deg,var(--green-mid),var(--green-deep))}
  .green.glow{background:linear-gradient(115deg,var(--green-deep),var(--green-light))}
  .lime.burst{background:linear-gradient(115deg,var(--lime-light) 20%,#eef4c8 60%,#fff 85%)}
  .lime.deep{background:linear-gradient(115deg,var(--lime-deep),var(--lime-mid))}
  .lime.glow{background:linear-gradient(115deg,var(--lime-light),var(--lime-mid))}
  .purple.burst{background:linear-gradient(115deg,var(--purple-mid) 20%,#e8d3ea 60%,#fff 85%)}
  .purple.deep{background:linear-gradient(115deg,var(--purple-deep),var(--purple-mid))}
  .purple.glow{background:linear-gradient(115deg,var(--purple-light),var(--purple-deep))}
  .blue.burst{background:linear-gradient(115deg,var(--blue-mid) 20%,#cfe2f2 60%,#fff 85%)}
  .blue.deep{background:linear-gradient(115deg,var(--blue-deep),var(--blue-light))}
  .blue.glow{background:linear-gradient(115deg,var(--blue-light),var(--blue-deep))}

  .red.burst .wordmark{color:var(--red-deep)}
  .green.burst .wordmark{color:var(--green-deep)}
  .lime.burst .wordmark{color:var(--lime-deep)}
  .purple.burst .wordmark{color:var(--purple-deep)}
  .blue.burst .wordmark{color:var(--blue-deep)}
</style>
</head>
<body>
<main class="sheet">

  <div class="sticker col-1 row-1"><div class="card red burst">
    <div class="mascot" role="img" aria-label="Pickle mascot in a cap holding a game controller"></div>
    <div class="wordmark">Brightvale<br>Relish<br>Co</div>
    <div class="slogan">Bold Crunch Delight</div>
    <div class="social-band"><span class="social"><span class="dot"></span>@brightvalerelishco</span><span class="social"><span class="square"></span>brightvalerelishco</span></div>
  </div></div>
  <div class="sticker col-2 row-1"><div class="card red deep">
    <div class="mascot" role="img" aria-label="Pickle mascot in a cap holding a game controller"></div>
    <div class="wordmark">Brightvale<br>Relish<br>Co</div>
    <div class="slogan">Bold Crunch Delight</div>
    <div class="social-band"><span class="social"><span class="dot"></span>@brightvalerelishco</span><span class="social"><span class="square"></span>brightvalerelishco</span></div>
  </div></div>
  <div class="sticker col-3 row-1"><div class="card red glow">
    <div class="mascot" role="img" aria-label="Pickle mascot in a cap holding a game controller"></div>
    <div class="wordmark">Brightvale<br>Relish<br>Co</div>
    <div class="slogan">Bold Crunch Delight</div>
    <div class="social-band"><span class="social"><span class="dot"></span>@brightvalerelishco</span><span class="social"><span class="square"></span>brightvalerelishco</span></div>
  </div></div>

  <div class="sticker col-1 row-2"><div class="card green burst">
    <div class="mascot" role="img" aria-label="Pickle mascot in a cap holding a game controller"></div>
    <div class="wordmark">Brightvale<br>Relish<br>Co</div>
    <div class="slogan">Bold Crunch Delight</div>
    <div class="social-band"><span class="social"><span class="dot"></span>@brightvalerelishco</span><span class="social"><span class="square"></span>brightvalerelishco</span></div>
  </div></div>
  <div class="sticker col-2 row-2"><div class="card green deep">
    <div class="mascot" role="img" aria-label="Pickle mascot in a cap holding a game controller"></div>
    <div class="wordmark">Brightvale<br>Relish<br>Co</div>
    <div class="slogan">Bold Crunch Delight</div>
    <div class="social-band"><span class="social"><span class="dot"></span>@brightvalerelishco</span><span class="social"><span class="square"></span>brightvalerelishco</span></div>
  </div></div>
  <div class="sticker col-3 row-2"><div class="card green glow">
    <div class="mascot" role="img" aria-label="Pickle mascot in a cap holding a game controller"></div>
    <div class="wordmark">Brightvale<br>Relish<br>Co</div>
    <div class="slogan">Bold Crunch Delight</div>
    <div class="social-band"><span class="social"><span class="dot"></span>@brightvalerelishco</span><span class="social"><span class="square"></span>brightvalerelishco</span></div>
  </div></div>

  <div class="sticker col-1 row-3"><div class="card lime burst">
    <div class="mascot" role="img" aria-label="Pickle mascot in a cap holding a game controller"></div>
    <div class="wordmark">Brightvale<br>Relish<br>Co</div>
    <div class="slogan">Bold Crunch Delight</div>
    <div class="social-band"><span class="social"><span class="dot"></span>@brightvalerelishco</span><span class="social"><span class="square"></span>brightvalerelishco</span></div>
  </div></div>
  <div class="sticker col-2 row-3"><div class="card lime deep">
    <div class="mascot" role="img" aria-label="Pickle mascot in a cap holding a game controller"></div>
    <div class="wordmark">Brightvale<br>Relish<br>Co</div>
    <div class="slogan">Bold Crunch Delight</div>
    <div class="social-band"><span class="social"><span class="dot"></span>@brightvalerelishco</span><span class="social"><span class="square"></span>brightvalerelishco</span></div>
  </div></div>
  <div class="sticker col-3 row-3"><div class="card lime glow">
    <div class="mascot" role="img" aria-label="Pickle mascot in a cap holding a game controller"></div>
    <div class="wordmark">Brightvale<br>Relish<br>Co</div>
    <div class="slogan">Bold Crunch Delight</div>
    <div class="social-band"><span class="social"><span class="dot"></span>@brightvalerelishco</span><span class="social"><span class="square"></span>brightvalerelishco</span></div>
  </div></div>

  <div class="sticker col-1 row-4"><div class="card purple burst">
    <div class="mascot" role="img" aria-label="Pickle mascot in a cap holding a game controller"></div>
    <div class="wordmark">Brightvale<br>Relish<br>Co</div>
    <div class="slogan">Bold Crunch Delight</div>
    <div class="social-band"><span class="social"><span class="dot"></span>@brightvalerelishco</span><span class="social"><span class="square"></span>brightvalerelishco</span></div>
  </div></div>
  <div class="sticker col-2 row-4"><div class="card purple deep">
    <div class="mascot" role="img" aria-label="Pickle mascot in a cap holding a game controller"></div>
    <div class="wordmark">Brightvale<br>Relish<br>Co</div>
    <div class="slogan">Bold Crunch Delight</div>
    <div class="social-band"><span class="social"><span class="dot"></span>@brightvalerelishco</span><span class="social"><span class="square"></span>brightvalerelishco</span></div>
  </div></div>
  <div class="sticker col-3 row-4"><div class="card purple glow">
    <div class="mascot" role="img" aria-label="Pickle mascot in a cap holding a game controller"></div>
    <div class="wordmark">Brightvale<br>Relish<br>Co</div>
    <div class="slogan">Bold Crunch Delight</div>
    <div class="social-band"><span class="social"><span class="dot"></span>@brightvalerelishco</span><span class="social"><span class="square"></span>brightvalerelishco</span></div>
  </div></div>

  <div class="sticker col-1 row-5"><div class="card blue burst">
    <div class="mascot" role="img" aria-label="Pickle mascot in a cap holding a game controller"></div>
    <div class="wordmark">Brightvale<br>Relish<br>Co</div>
    <div class="slogan">Bold Crunch Delight</div>
    <div class="social-band"><span class="social"><span class="dot"></span>@brightvalerelishco</span><span class="social"><span class="square"></span>brightvalerelishco</span></div>
  </div></div>
  <div class="sticker col-2 row-5"><div class="card blue deep">
    <div class="mascot" role="img" aria-label="Pickle mascot in a cap holding a game controller"></div>
    <div class="wordmark">Brightvale<br>Relish<br>Co</div>
    <div class="slogan">Bold Crunch Delight</div>
    <div class="social-band"><span class="social"><span class="dot"></span>@brightvalerelishco</span><span class="social"><span class="square"></span>brightvalerelishco</span></div>
  </div></div>
  <div class="sticker col-3 row-5"><div class="card blue glow">
    <div class="mascot" role="img" aria-label="Pickle mascot in a cap holding a game controller"></div>
    <div class="wordmark">Brightvale<br>Relish<br>Co</div>
    <div class="slogan">Bold Crunch Delight</div>
    <div class="social-band"><span class="social"><span class="dot"></span>@brightvalerelishco</span><span class="social"><span class="square"></span>brightvalerelishco</span></div>
  </div></div>

</main>
</body>
</html>
```